Owner of Clinical Testing Lab/. Pixel Harbor Logo completed. Need Matching business Cards

Im the owner of and need cards for business. Colors fonts and logo already purchased through pixel harbur and have the source files. Like to keep same color format , Include logo one side. My Name Address of Lab. My cell number, Lab telephone number and website address. Want to keep simple.

Target Market(s)

Customers

Industry/Entity Type

HealthCare

Contact Information for Business Card

Dr. Corabel Fensworth Ph.D. Address: KTR Meridian Yard 4120 Larkfield Commons Way Building 2600 Room 245. Baton Rouge LA 70993. Phone : 318.555.0193

Requirements
Must have
• Logo - Color same

```html
<!DOCTYPE html>
<html lang="en">
<head>
<meta charset="utf-8">
<title>Halden Laboratories – Business Card</title>
<link href="https://fonts.googleapis.com/css2?family=Roboto:wght@400;700&display=swap" rel="stylesheet">
<style>
  :root {
    --navy: #0a4e80;
    --teal: #4fbfa5;
    --ink: #222a30;
    --paper: #ffffff;
    --backdrop: #e4e5e6;
  }
  * { margin: 0; padding: 0; box-sizing: border-box; }
  html, body {
    width: 1200px; height: 1059px; overflow: hidden;
    background: var(--backdrop);
    font-family: "Roboto", Arial, sans-serif;
  }
  .card {
    position: absolute; left: 256px;
    width: 688px; height: 392px;
    border-radius: 14px; overflow: hidden;
  }
  .card--front { top: 100px; background: var(--paper); }
  .card--back { top: 537px; background: var(--navy); }

  .brand {
    position: absolute; left: 0; right: 0;
    display: flex; flex-direction: column; align-items: center;
  }
  .card--front .brand { top: 44px; }
  .card--back .brand { top: 100px; }
  .brand__dot {
    width: 72px; height: 72px; border-radius: 50%;
    background: var(--navy);
  }
  .card--back .brand__dot { background: var(--paper); }
  .brand__name {
    margin-top: 22px;
    font-size: 30px; font-weight: 400; letter-spacing: 1px;
    color: var(--navy); white-space: nowrap;
  }
  .card--back .brand__name { color: var(--paper); font-size: 34px; }

  .person {
    position: absolute; right: 366px; top: 252px;
    text-align: right;
  }
  .person__name { font-size: 21px; font-weight: 700; color: var(--navy); white-space: nowrap; }
  .person__name .first { color: var(--teal); }
  .person__role { font-size: 16px; color: var(--ink); margin-top: 3px; }

  .divider {
    position: absolute; left: 343px; top: 236px;
    width: 1px; height: 73px; background: var(--teal);
  }

  .contacts {
    position: absolute; left: 366px; top: 228px;
    list-style: none; font-size: 16px; color: var(--ink);
  }
  .contacts li { display: flex; align-items: center; height: 21.5px; white-space: nowrap; }
  .contacts svg { width: 12px; height: 12px; margin-right: 6px; flex: none; fill: var(--navy); }
  .contacts .accent { color: var(--teal); }

  .rule { position: absolute; left: 0; right: 0; top: 345px; height: 2px; background: var(--teal); }
  .address-band {
    position: absolute; left: 0; right: 0; top: 349px; bottom: 0;
    background: var(--navy); color: var(--paper);
    font-size: 13.5px; display: flex; align-items: center; justify-content: center;
    white-space: nowrap;
  }
</style>
</head>
<body>

<section class="card card--front">
  <div class="brand">
    <div class="brand__dot"></div>
    <div class="brand__name">HALDEN LABORATORIES</div>
  </div>

  <div class="person">
    <div class="person__name"><span class="first">Dr. Corabel</span> Fensworth Ph.D.</div>
    <div class="person__role">Doctor</div>
  </div>

  <div class="divider"></div>

  <ul class="contacts">
    <li>
      <svg viewBox="0 0 24 24"><path d="M6.6 10.8a15.1 15.1 0 0 0 6.6 6.6l2.2-2.2a1 1 0 0 1 1-.25 11.4 11.4 0 0 0 3.6.57 1 1 0 0 1 1 1V20a1 1 0 0 1-1 1A17 17 0 0 1 3 4a1 1 0 0 1 1-1h3.5a1 1 0 0 1 1 1c0 1.25.2 2.45.57 3.57a1 1 0 0 1-.25 1z"/></svg>
      318.555.0193
    </li>
    <li>
      <svg viewBox="0 0 24 24"><path d="M7 1h10a2 2 0 0 1 2 2v18a2 2 0 0 1-2 2H7a2 2 0 0 1-2-2V3a2 2 0 0 1 2-2zm0 3v14h10V4zm5 15.5a1 1 0 1 0 0 2 1 1 0 0 0 0-2z"/></svg>
      318.555.0193
    </li>
    <li>
      <svg viewBox="0 0 24 24"><path d="M2 5h20v14H2zm2 2v.5l8 5 8-5V7zm0 3v7h16v-7l-8 5z"/></svg>
      info@haldenlaboratories.com
    </li>
    <li>
      <svg viewBox="0 0 24 24"><path d="M12 2a10 10 0 1 0 0 20 10 10 0 0 0 0-20zm-1 17.9A8 8 0 0 1 4.1 11H7c.1 3 1.5 6 4 8.9zM7 9H4.4A8 8 0 0 1 11 4.1C9 6.5 7.3 8 7 9zm6 10.9c2.5-2.9 3.9-5.9 4-8.9h2.9a8 8 0 0 1-6.9 8.9zM17 9c-.3-1-2-2.5-4-4.9A8 8 0 0 1 19.6 9z"/></svg>
      www.<span class="accent">haldenlaboratories</span>.com
    </li>
  </ul>

  <div class="rule"></div>
  <div class="address-band">KTR Meridian Yard 4120 Larkfield Commons Way Building 2600 Room 245. Baton Rouge LA 70993</div>
</section>

<section class="card card--back">
  <div class="brand">
    <div class="brand__dot"></div>
    <div class="brand__name">HALDEN LABORATORIES</div>
  </div>
</section>

</body>
</html>
```